Crypto Exchange Comparison Platform

Let’s design a page that lets users compare hundreds of cryptocurrency exchanges. It will help users compare more info than anywhere else so you can find the best crypto exchange for your needs. The goal is to transform complex data into a clean, visually engaging experience.

Key Features to Design:
- Interactive comparison table with ~ 30 columns
- Filters and dropdown menus for easier usability
- Summary boxes for quick-view statistics
- Visual charts and graphs for key metrics
- Web, mobile, and tablet responsive design

Design Goals:
- Clean, modern aesthetic that makes complex data easily digestible
- Interactive elements (eg. Bar and Spider charts) for user engagement
- "Screenshot-friendly" sections for social media and sharing
- Data visualization focus (charts, graphs, metrics)
- Extremely easy to use on mobile
- Designs that use the color green
- A brand that communicates research and trusted information

Deliverables:
- High-fidelity mockup for desktop, tablet, and mobile versions
- Interactive prototype (Figma preferred)
- Style guide (typography, colors, components)

Note: The goal is to create an intuitive, visually engaging tool that helps users compare cryptocurrency exchanges efficiently while maintaining a clean, professional appearance that works well for social media sharing and content creation.
Updates

Low design quality

Industry/Entity Type

FinTech, Crypto, Finance

Number of Pages Required

1 page

Other font styles liked:
• Inter or something good for a finance/data related website site

Colors
00AB8E
00BBA5
67D7C9
C6EFE9
E9F9F6

Requirements
Must have
• Please refer to the sketch I uploaded

```html
<!DOCTYPE html>
<html lang="en">
<head>
<meta charset="utf-8">
<title>Crypto Exchange – Compare Crypto Exchanges</title>
<link href="https://fonts.googleapis.com/css2?family=Inter:wght@400;500;600;700&family=Poppins:wght@400;500;600;700&display=swap" rel="stylesheet">
<style>
:root{
  --green:#00AB8E;
  --teal:#00BBA5;
  --mint:#67D7C9;
  --pale:#C6EFE9;
  --wash:#E9F9F6;
  --row:#F3FBF9;
  --ink:#1B2A33;
  --muted:#6B7A80;
  --line:#D7EEEA;
  --white:#fff;
}
*{box-sizing:border-box;margin:0;padding:0}
html,body{width:1200px;height:4721px;overflow:hidden;background:#fff}
body{font-family:"Inter",sans-serif;color:var(--ink)}
.page{position:relative;width:1200px;height:4721px;overflow:hidden}
.abs{position:absolute}
h1,h2,h3,.brand,.poppins{font-family:"Poppins",sans-serif}

/* header */
.site-header{position:absolute;left:0;top:0;width:1200px;height:77px;border-bottom:1px solid var(--pale);background:#fff;z-index:2}
.brand{position:absolute;left:106px;top:24px;font-size:25px;font-weight:500;color:var(--ink)}
.brand span{color:var(--green);font-weight:600}
.main-nav a{position:absolute;top:33px;font-size:13px;font-weight:500;color:var(--ink);text-decoration:none}
.btn-start{position:absolute;left:963px;top:23px;width:131px;height:37px;border-radius:19px;background:var(--green);color:#fff;font-size:13px;font-weight:600;display:flex;align-items:center;justify-content:center;box-shadow:0 0 0 3px var(--pale)}

/* hero */
.hero{position:absolute;left:0;top:77px;width:1200px;height:420px;background:linear-gradient(100deg,#fff 35%,#EEFAF8 70%,#D9F4EF 100%)}
.hero-title{position:absolute;left:0;width:1200px;top:116px;text-align:center;font-size:50px;font-weight:500;letter-spacing:.5px}
.hero-title mark{background:var(--teal);color:#fff;padding:0 14px;font-weight:500}
.hero-sub{position:absolute;left:270px;width:660px;top:196px;text-align:center;font-size:20px;line-height:31px;color:var(--ink)}
.chip{position:absolute;top:298px;width:283px;height:58px;border:2px solid var(--pale);background:#fff;display:flex;align-items:center;justify-content:center;gap:10px;font-size:17px;font-weight:500}

/* section heading with rule */
.rule{position:absolute;height:2px;background:var(--green)}
.rule::after{content:"";position:absolute;right:-4px;top:-3px;width:8px;height:8px;border-radius:50%;background:var(--green)}
.sec-title{position:absolute;font-size:32px;font-weight:600}

/* top picks */
.pick{position:absolute;top:621px;width:322px;height:154px;background:#fff;border:1px solid var(--pale);box-shadow:0 6px 16px rgba(0,171,142,.10)}
.pick .logo{position:absolute;left:33px;top:22px;width:54px;height:54px;border-radius:50%}
.pick h3{position:absolute;left:103px;top:26px;font-size:21px;font-weight:600}
.pick .desc{position:absolute;left:103px;top:60px;font-size:14px;color:#9aa6aa}
.pick .url{position:absolute;left:103px;top:85px;font-size:14px;display:flex;gap:6px;align-items:center}
.pick svg.spark{position:absolute;right:10px;bottom:12px}

/* tabs */
.tab{position:absolute;top:854px;height:42px;width:145px;border:1px solid var(--pale);display:flex;align-items:center;justify-content:center;gap:8px;font-size:14px;font-weight:500;color:var(--green);background:#fff}
.tab.active{background:var(--green);color:#fff;border-color:var(--green)}
.select{position:absolute;height:42px;border:1px solid var(--pale);background:#fff;display:flex;align-items:center;justify-content:space-between;padding:0 14px;font-size:14px;font-weight:500}

/* table */
.table-wrap{position:absolute;left:95px;top:938px;width:1030px;height:1017px;border:1px solid var(--pale);background:#fff}
.fee-table{width:100%;border-collapse:collapse;font-size:11px;table-layout:fixed}
.fee-table th{height:60px;font-weight:600;font-size:11.5px;text-align:left;padding-top:4px}
.fee-table td{height:37px}
.fee-table tbody tr:nth-child(even){background:var(--row)}
.fee-table th:first-child,.fee-table td:first-child{text-align:center}
.ex{display:flex;align-items:center;gap:6px;font-size:9.5px}
.ex i{display:inline-block;width:13px;height:13px;border-radius:50%}
.c1{background:#F3BA2F}.c2{background:#1652F0}.c3{background:#111}.c4{background:#2b3a4d}.c5{background:#5741D9}.c6{background:#2354E6}.c7{background:var(--teal)}.c8{background:#222}

.pager{position:absolute;top:1974px;left:500px;display:flex;gap:0;align-items:center;font-size:12px}
.pager span{width:30px;height:28px;display:flex;align-items:center;justify-content:center;margin-right:6px}
.pager .on{background:var(--wash);color:var(--green);border-radius:4px;font-weight:600}

/* charts */
.card{position:absolute;background:#fff;border:2px solid var(--pale)}
.chart-title{position:absolute;left:30px;top:24px;display:flex;align-items:center;gap:12px;font-size:21px;font-weight:500}
.stat{position:absolute;top:2468px;height:166px;width:236px;border:2px solid var(--pale);background:#fff;overflow:hidden}
.stat .lbl{position:absolute;left:24px;top:22px;font-size:15px;font-weight:500}
.stat .num{position:absolute;left:22px;top:50px;font-size:42px;font-weight:600;color:var(--teal);font-family:"Poppins",sans-serif}
.stat .note{position:absolute;left:26px;top:50px;font-size:9px}
.stat.dark{background:var(--green);border-color:var(--green);color:#fff}
.stat.dark .num{color:#fff;top:70px}
.stat.light{background:#DDF5F0;border-color:#DDF5F0}
.stat.light .num{top:70px}

/* compare */
.compare-bg{position:absolute;left:0;top:2711px;width:1200px;height:953px;background:var(--wash)}
.panel{position:absolute;background:#fff;box-shadow:0 6px 18px rgba(0,171,142,.08)}
.score-table{position:absolute;left:33px;top:296px;width:273px;font-size:12px;border-collapse:collapse}
.score-table th{height:36px;background:var(--wash);font-weight:500;font-size:12px}
.score-table td{height:44px;border-bottom:1px solid #e3ecea}
.score-table td:first-child{color:var(--green);padding-left:12px}
.acc-head{position:absolute;left:44px;width:550px;display:flex;align-items:center;gap:12px;font-size:16px;font-weight:600;letter-spacing:.5px}
.acc-head svg.chev{position:absolute;right:0}
.acc-line{position:absolute;left:32px;width:556px;height:1px;background:#e3ecea}
.feat-row{position:absolute;left:30px;width:562px;height:44px;display:flex;align-items:center;font-size:15px}
.feat-row.shade{background:#EEF3F2}
.feat-row span:nth-child(1){width:225px;padding-left:20px}
.feat-row span:nth-child(2){width:225px}

/* faq */
.faq-title{position:absolute;left:0;width:1200px;top:3746px;text-align:center;font-size:34px;font-weight:600}
.faq-title span{font-weight:400}
.faq{position:absolute;left:178px;width:866px;height:64px;border:2px solid var(--pale);background:#fff;font-size:17px;font-weight:600;padding-left:38px;display:flex;align-items:center}
.faq svg{position:absolute;right:22px;top:24px}
.faq.open{height:136px;border-color:var(--mint);align-items:flex-start;flex-direction:column;padding-top:28px}
.faq.open p{font-size:12px;font-weight:400;color:var(--muted);line-height:19px;margin-top:14px;padding-left:2px;width:760px}

/* footer */
.site-footer{position:absolute;left:0;top:4384px;width:1200px;height:337px;background:linear-gradient(120deg,#18B9A4,#00A88D 60%,#008C77);color:#fff}
.site-footer .fbrand{position:absolute;left:119px;top:74px;font-size:24px;font-weight:500}
.site-footer .fabout{position:absolute;left:119px;top:128px;width:250px;font-size:12px;line-height:23px}
.site-footer .copy{position:absolute;left:119px;top:228px;font-size:12px;opacity:.9}
.fcol{position:absolute;top:67px}
.fcol h4{font-size:18px;font-weight:600;border-left:3px solid #fff;padding-left:10px;line-height:20px}
.fcol a{display:block;color:#fff;text-decoration:none;font-size:12px;line-height:23px;margin-left:16px}
.fcol a:first-of-type{margin-top:12px}
.social{position:absolute;top:120px;display:flex;gap:28px;left:911px}
.social i{display:block;width:24px;height:24px;border-radius:50%;background:#fff}
</style>
</head>
<body>
<div class="page">

<header class="site-header">
  <div class="brand">Crypto <span>Exchange</span></div>
  <nav class="main-nav">
    <a href="#" style="left:370px">Crypto Currencies</a>
    <a href="#" style="left:518px">Exchanges</a>
    <a href="#" style="left:621px">Learn</a>
    <a href="#" style="left:689px">How it Works</a>
    <a href="#" style="left:806px">API</a>
    <a href="#" style="left:863px">Resources</a>
  </nav>
  <a class="btn-start" href="#">Get Started</a>
</header>

<section class="hero">
  <h1 class="hero-title">Compare Crypto <mark>Exchange</mark></h1>
  <p class="hero-sub">Lorem ipsum dolor sit amet, consectetur adipiscing elit, sed do eiusmod tempor incididunt ut labore et dolore</p>
  <div class="chip" style="left:170px">
    <svg width="20" height="18" viewBox="0 0 20 18"><path d="M1 1v16h18" stroke="#00AB8E" stroke-width="2" fill="none"/><rect x="5" y="8" width="3" height="7" fill="#00AB8E"/><rect x="10" y="4" width="3" height="11" fill="#00AB8E"/><rect x="15" y="9" width="3" height="6" fill="#00AB8E"/></svg>
    Platform Tracked: 125</div>
  <div class="chip" style="left:469px">
    <svg width="20" height="20" viewBox="0 0 20 20"><rect x="2" y="4" width="16" height="14" rx="2" stroke="#00AB8E" stroke-width="2" fill="none"/><path d="M2 8h16M6 1v5M14 1v5" stroke="#00AB8E" stroke-width="2"/></svg>
    Updated: Feb 16, 2025</div>
  <div class="chip" style="left:768px">
    <svg width="24" height="20" viewBox="0 0 24 20"><circle cx="9" cy="6" r="5" fill="#00AB8E"/><path d="M0 19c0-6 4-8 9-8s9 2 9 8z" fill="#00AB8E"/><circle cx="19" cy="14" r="4" fill="#fff" stroke="#00AB8E" stroke-width="2"/></svg>
    How We Test</div>
</section>

<div class="rule" style="left:0;top:573px;width:80px"></div>
<h2 class="sec-title" style="left:102px;top:552px">Top Picks</h2>

<div class="pick" style="left:102px">
  <div class="logo" style="background:var(--green)"></div>
  <h3>Pylonex</h3><div class="desc">Lorem ipsum dolor sit</div>
  <div class="url"><svg width="12" height="12" viewBox="0 0 12 12"><circle cx="6" cy="6" r="5" stroke="#00AB8E" fill="none"/><path d="M1 6h10M6 1c3 3 3 7 0 10M6 1c-3 3-3 7 0 10" stroke="#00AB8E" fill="none"/></svg>www.pylonex.test</div>
  <svg class="spark" width="140" height="40" viewBox="0 0 140 40"><path d="M0 38 L20 26 L34 32 L52 14 L66 24 L84 8 L100 22 L118 12 L140 20 L140 40 L0 40Z" fill="#E9F9F6"/><path d="M0 38 L20 26 L34 32 L52 14 L66 24 L84 8 L100 22 L118 12 L140 20" stroke="#C6EFE9" fill="none"/></svg>
</div>
<div class="pick" style="left:445px">
  <div class="logo" style="background:var(--teal)"></div>
  <h3>Extendra Up</h3><div class="desc">Lorem ipsum dolor sit</div>
  <div class="url"><svg width="12" height="12" viewBox="0 0 12 12"><circle cx="6" cy="6" r="5" stroke="#00AB8E" fill="none"/><path d="M1 6h10M6 1c3 3 3 7 0 10M6 1c-3 3-3 7 0 10" stroke="#00AB8E" fill="none"/></svg>www.pylonex.test</div>
  <svg class="spark" width="140" height="40" viewBox="0 0 140 40"><path d="M0 38 L20 26 L34 32 L52 14 L66 24 L84 8 L100 22 L118 12 L140 20 L140 40 L0 40Z" fill="#E9F9F6"/><path d="M0 38 L20 26 L34 32 L52 14 L66 24 L84 8 L100 22 L118 12 L140 20" stroke="#C6EFE9" fill="none"/></svg>
</div>
<div class="pick" style="left:791px">
  <div class="logo" style="background:#F2A516"></div>
  <h3>Kelpie</h3><div class="desc">Lorem ipsum dolor sit</div>
  <div class="url"><svg width="12" height="12" viewBox="0 0 12 12"><circle cx="6" cy="6" r="5" stroke="#00AB8E" fill="none"/><path d="M1 6h10M6 1c3 3 3 7 0 10M6 1c-3 3-3 7 0 10" stroke="#00AB8E" fill="none"/></svg>www.pylonex.test</div>
  <svg class="spark" width="140" height="40" viewBox="0 0 140 40"><path d="M0 38 L20 26 L34 32 L52 14 L66 24 L84 8 L100 22 L118 12 L140 20 L140 40 L0 40Z" fill="#E9F9F6"/><path d="M0 38 L20 26 L34 32 L52 14 L66 24 L84 8 L100 22 L118 12 L140 20" stroke="#C6EFE9" fill="none"/></svg>
</div>

<div class="tab active" style="left:95px"><svg width="18" height="18" viewBox="0 0 18 18"><circle cx="9" cy="9" r="8" fill="#fff"/><text x="9" y="13" font-size="11" font-weight="700" text-anchor="middle" fill="#00AB8E" font-family="Inter,sans-serif">$</text></svg>Fees</div>
<div class="tab" style="left:247px"><svg width="16" height="14" viewBox="0 0 16 14"><rect x="1" y="8" width="4" height="5" fill="#67D7C9"/><rect x="6" y="3" width="4" height="10" fill="#00AB8E"/><rect x="11" y="6" width="4" height="7" fill="#67D7C9"/></svg>Features</div>
<div class="tab" style="left:399px"><svg width="14" height="16" viewBox="0 0 14 16"><path d="M7 1L1 3.5V8c0 3.5 3 6 6 7 3-1 6-3.5 6-7V3.5z" fill="#67D7C9"/></svg>Security</div>
<div class="select" style="left:971px;top:854px;width:143px"><span style="display:flex;gap:8px;align-items:center"><svg width="14" height="14" viewBox="0 0 14 14"><path d="M2 12l4-4M8 6l4-4M9 2h3v3M5 12H2V9" stroke="#00AB8E" stroke-width="1.5" fill="none"/></svg>Compare</span><svg width="12" height="8" viewBox="0 0 12 8"><path d="M1 1l5 5 5-5" stroke="#00AB8E" stroke-width="2" fill="none"/></svg></div>

<div class="table-wrap">
<table class="fee-table">
  <colgroup><col style="width:83px"><col style="width:111px"><col style="width:101px"><col style="width:99px"><col style="width:143px"><col style="width:137px"><col style="width:152px"><col style="width:94px"><col></colgroup>
  <thead><tr><th>#</th><th>Exchange</th><th>Maker Fee</th><th>Taker Fee</th><th>Futures Maker Fee</th><th>Futures Taker Fee</th><th>Trading Fee Discount</th><th>Discount</th><th>Visit</th></tr></thead>
  <tbody>
<tr><td>1</td><td><span class="ex"><i class="c1"></i>Binova</span></td><td>$12.50</td><td>$8.50</td><td>$6.50</td><td>$4.80</td><td>$2.50</td><td>5%</td><td>www.lnk.test</td></tr>
<tr><td>2</td><td><span class="ex"><i class="c2"></i>Coinvale</span></td><td>$12.50</td><td>$8.50</td><td>$6.50</td><td>$4.80</td><td>$2.50</td><td>5%</td><td>www.lnk.test</td></tr>
<tr><td>3</td><td><span class="ex"><i class="c3"></i>Okra</span></td><td>$12.50</td><td>$8.50</td><td>$6.50</td><td>$4.80</td><td>$2.50</td><td>5%</td><td>www.lnk.test</td></tr>
<tr><td>4</td><td><span class="ex"><i class="c4"></i>Cryptora</span></td><td>$12.50</td><td>$8.50</td><td>$6.50</td><td>$4.80</td><td>$2.50</td><td>5%</td><td>www.lnk.test</td></tr>
<tr><td>5</td><td><span class="ex"><i class="c5"></i>Kelpie</span></td><td>$12.50</td><td>$8.50</td><td>$6.50</td><td>$4.80</td><td>$2.50</td><td>5%</td><td>www.lnk.test</td></tr>
<tr><td>6</td><td><span class="ex"><i class="c6"></i>Gatewise</span></td><td>$12.50</td><td>$8.50</td><td>$6.50</td><td>$4.80</td><td>$2.50</td><td>5%</td><td>www.lnk.test</td></tr>
<tr><td>7</td><td><span class="ex"><i class="c7"></i>Bitgrid Exchange</span></td><td>$12.50</td><td>$8.50</td><td>$6.50</td><td>$4.80</td><td>$2.50</td><td>5%</td><td>www.lnk.test</td></tr>
<tr><td>8</td><td><span class="ex"><i class="c8"></i>Bitstone</span></td><td>$12.50</td><td>$8.50</td><td>$6.50</td><td>$4.80</td><td>$2.50</td><td>5%</td><td>www.lnk.test</td></tr>
<tr><td>9</td><td><span class="ex"><i class="c1"></i>Binova</span></td><td>$12.50</td><td>$8.50</td><td>$6.50</td><td>$4.80</td><td>$2.50</td><td>5%</td><td>www.lnk.test</td></tr>
<tr><td>10</td><td><span class="ex"><i class="c2"></i>Coinvale</span></td><td>$12.50</td><td>$8.50</td><td>$6.50</td><td>$4.80</td><td>$2.50</td><td>5%</td><td>www.lnk.test</td></tr>
<tr><td>11</td><td><span class="ex"><i class="c3"></i>Okra</span></td><td>$12.50</td><td>$8.50</td><td>$6.50</td><td>$4.80</td><td>$2.50</td><td>5%</td><td>www.lnk.test</td></tr>
<tr><td>12</td><td><span class="ex"><i class="c4"></i>Cryptora</span></td><td>$12.50</td><td>$8.50</td><td>$6.50</td><td>$4.80</td><td>$2.50</td><td>5%</td><td>www.lnk.test</td></tr>
<tr><td>13</td><td><span class="ex"><i class="c5"></i>Kelpie</span></td><td>$12.50</td><td>$8.50</td><td>$6.50</td><td>$4.80</td><td>$2.50</td><td>5%</td><td>www.lnk.test</td></tr>
<tr><td>14</td><td><span class="ex"><i class="c6"></i>Gatewise</span></td><td>$12.50</td><td>$8.50</td><td>$6.50</td><td>$4.80</td><td>$2.50</td><td>5%</td><td>www.lnk.test</td></tr>
<tr><td>15</td><td><span class="ex"><i class="c7"></i>Bitgrid Exchange</span></td><td>$12.50</td><td>$8.50</td><td>$6.50</td><td>$4.80</td><td>$2.50</td><td>5%</td><td>www.lnk.test</td></tr>
<tr><td>16</td><td><span class="ex"><i class="c8"></i>Bitstone</span></td><td>$12.50</td><td>$8.50</td><td>$6.50</td><td>$4.80</td><td>$2.50</td><td>5%</td><td>www.lnk.test</td></tr>
<tr><td>17</td><td><span class="ex"><i class="c1"></i>Binova</span></td><td>$12.50</td><td>$8.50</td><td>$6.50</td><td>$4.80</td><td>$2.50</td><td>5%</td><td>www.lnk.test</td></tr>
<tr><td>18</td><td><span class="ex"><i class="c2"></i>Coinvale</span></td><td>$12.50</td><td>$8.50</td><td>$6.50</td><td>$4.80</td><td>$2.50</td><td>5%</td><td>www.lnk.test</td></tr>
<tr><td>19</td><td><span class="ex"><i class="c3"></i>Okra</span></td><td>$12.50</td><td>$8.50</td><td>$6.50</td><td>$4.80</td><td>$2.50</td><td>5%</td><td>www.lnk.test</td></tr>
<tr><td>20</td><td><span class="ex"><i class="c4"></i>Cryptora</span></td><td>$12.50</td><td>$8.50</td><td>$6.50</td><td>$4.80</td><td>$2.50</td><td>5%</td><td>www.lnk.test</td></tr>
<tr><td>21</td><td><span class="ex"><i class="c5"></i>Kelpie</span></td><td>$12.50</td><td>$8.50</td><td>$6.50</td><td>$4.80</td><td>$2.50</td><td>5%</td><td>www.lnk.test</td></tr>
<tr><td>22</td><td><span class="ex"><i class="c6"></i>Gatewise</span></td><td>$12.50</td><td>$8.50</td><td>$6.50</td><td>$4.80</td><td>$2.50</td><td>5%</td><td>www.lnk.test</td></tr>
<tr><td>23</td><td><span class="ex"><i class="c7"></i>Bitgrid Exchange</span></td><td>$12.50</td><td>$8.50</td><td>$6.50</td><td>$4.80</td><td>$2.50</td><td>5%</td><td>www.lnk.test</td></tr>
<tr><td>24</td><td><span class="ex"><i class="c8"></i>Bitstone</span></td><td>$12.50</td><td>$8.50</td><td>$6.50</td><td>$4.80</td><td>$2.50</td><td>5%</td><td>www.lnk.test</td></tr>
<tr><td>25</td><td><span class="ex"><i class="c4"></i>Cryptora</span></td><td>$12.50</td><td>$8.50</td><td>$6.50</td><td>$4.80</td><td>$2.50</td><td>5%</td><td>www.lnk.test</td></tr>
  </tbody>
</table>
</div>

<div class="pager">
  <span><svg width="8" height="12" viewBox="0 0 8 12"><path d="M6 1L1 6l5 5" stroke="#1B2A33" stroke-width="1.5" fill="none"/></svg></span>
  <span class="on">1</span><span>2</span><span>3</span><span>4</span><span>5</span>
  <span><svg width="8" height="12" viewBox="0 0 8 12"><path d="M2 1l5 5-5 5" stroke="#1B2A33" stroke-width="1.5" fill="none"/></svg></span>
</div>
<div class="abs" style="left:958px;top:1982px;font-size:11px">Show rows</div>
<div class="select" style="left:1037px;top:1975px;width:86px;height:29px;font-size:11px;padding:0 10px">25<svg width="11" height="7" viewBox="0 0 12 8"><path d="M1 1l5 5 5-5" stroke="#00AB8E" stroke-width="2" fill="none"/></svg></div>

<!-- Maker fees chart -->
<div class="card" style="left:121px;top:2088px;width:487px;height:359px">
  <div class="chart-title"><svg width="14" height="9" viewBox="0 0 14 9"><path d="M1 1l6 6 6-6" stroke="#00AB8E" stroke-width="2" fill="none"/></svg>Maker Fees</div>
  <svg class="abs" style="left:0;top:0" width="487" height="359" viewBox="0 0 487 359" font-family="Inter,sans-serif" font-size="10" fill="#1B2A33">
    <g stroke="#EEF3F2"><line x1="44" y1="88" x2="451" y2="88"/><line x1="44" y1="134" x2="451" y2="134"/><line x1="44" y1="180" x2="451" y2="180"/><line x1="44" y1="226" x2="451" y2="226"/><line x1="44" y1="273" x2="451" y2="273"/></g>
    <line x1="44" y1="319" x2="451" y2="319" stroke="#1B2A33" stroke-width="1"/>
    <g text-anchor="end"><text x="36" y="92">30</text><text x="36" y="138">25</text><text x="36" y="184">20</text><text x="36" y="230">10</text><text x="36" y="277">5</text><text x="36" y="323">0</text></g>
    <g>
      <rect x="53" y="277" width="12" height="42" fill="#C6EFE9"/>
      <rect x="80" y="230" width="12" height="89" fill="#00AB8E"/>
      <rect x="111" y="126" width="12" height="193" fill="#00AB8E"/>
      <rect x="141" y="257" width="12" height="62" fill="#C6EFE9"/>
      <rect x="166" y="142" width="12" height="177" fill="#67D7C9"/>
      <rect x="194" y="277" width="12" height="42" fill="#00AB8E"/>
      <rect x="221" y="246" width="12" height="73" fill="#C6EFE9"/>
      <rect x="256" y="80" width="12" height="239" fill="#00AB8E"/>
      <rect x="283" y="257" width="12" height="62" fill="#00AB8E"/>
      <rect x="307" y="277" width="12" height="42" fill="#C6EFE9"/>
      <rect x="335" y="146" width="12" height="173" fill="#67D7C9"/>
      <rect x="370" y="173" width="12" height="146" fill="#00AB8E"/>
      <rect x="399" y="277" width="12" height="42" fill="#C6EFE9"/>
      <rect x="428" y="107" width="12" height="212" fill="#00AB8E"/>
    </g>
    <g font-size="8" text-anchor="middle" fill="#6B7A80"><text x="66" y="338">2016</text><text x="112" y="338">2017</text><text x="159" y="338">2018</text><text x="207" y="338">2019</text><text x="255" y="338">2020</text><text x="302" y="338">2021</text><text x="353" y="338">2022</text><text x="399" y="338">2023</text><text x="438" y="338">2024</text></g>
  </svg>
</div>

<!-- Trading volume chart -->
<div class="card" style="left:623px;top:2088px;width:489px;height:359px;overflow:hidden">
  <svg class="abs" style="left:0;top:0" width="489" height="359" viewBox="0 0 489 359">
    <g stroke="#F0F4F3"><path d="M300 0V359M360 0V359M420 0V359M480 0V359M240 60H489M240 120H489M240 180H489M240 240H489M240 300H489"/></g>
    <defs><linearGradient id="vol" x1="0" y1="0" x2="0" y2="1"><stop offset="0" stop-color="#C6EFE9"/><stop offset="1" stop-color="#fff" stop-opacity="0"/></linearGradient></defs>
    <path d="M2 260 L38 214 L68 253 L103 183 L125 213 L145 183 L183 238 L218 145 L234 165 L266 143 L300 183 L368 88 L449 165 L469 147 L484 158 L489 160 L489 359 L0 359Z" fill="url(#vol)"/>
    <path d="M2 260 L38 214 L68 253 L103 183 L125 213 L145 183 L183 238 L218 145 L234 165 L266 143 L300 183 L368 88 L449 165 L469 147 L484 158 L489 160" stroke="#00BBA5" stroke-width="2" fill="none"/>
    <g fill="#fff" stroke="#00BBA5" stroke-width="2"><circle cx="38" cy="214" r="4"/><circle cx="145" cy="183" r="4"/><circle cx="218" cy="145" r="4"/><circle cx="300" cy="183" r="4"/><circle cx="368" cy="88" r="4"/><circle cx="449" cy="165" r="4"/></g>
  </svg>
  <div class="chart-title"><svg width="14" height="9" viewBox="0 0 14 9"><path d="M1 1l6 6 6-6" stroke="#00AB8E" stroke-width="2" fill="none"/></svg>Trading Volume</div>
</div>

<div class="stat" style="left:123px">
  <div class="lbl">Exchange Tracked</div><div class="num">125</div>
  <svg class="abs" style="left:14px;top:96px" width="210" height="60" viewBox="0 0 210 60"><path d="M0 52 C20 30 30 50 50 34 S80 40 100 30 S130 44 150 30 S190 36 210 40 V60 H0Z" fill="#E9F9F6"/><path d="M0 52 C20 30 30 50 50 34 S80 40 100 30 S130 44 150 30 S190 36 210 40" stroke="#67D7C9" stroke-width="2" fill="none"/></svg>
</div>
<div class="stat" style="left:376px">
  <div class="lbl">Average Trading Fee</div><div class="num">0.15%</div>
  <svg class="abs" style="left:30px;top:96px" width="200" height="60" viewBox="0 0 200 60"><path d="M0 56 C30 50 40 20 70 30 S100 56 120 34 S160 10 200 24" stroke="#C6EFE9" stroke-width="2" fill="none"/><path d="M20 58 C50 30 70 50 100 20 S150 40 190 20" stroke="#DCE6E4" stroke-width="1.5" fill="none"/></svg>
</div>
<div class="stat dark" style="left:623px">
  <div class="lbl">Total Users</div><div class="note">Lorem ipsum dolor sit amet, consectetur</div><div class="num">892M</div>
</div>
<div class="stat light" style="left:872px">
  <div class="lbl">Web Visitor (30D)</div><div class="note">Lorem ipsum dolor sit amet, consectetur</div><div class="num">12.2B</div>
</div>

<!-- Compare -->
<div class="compare-bg"></div>
<div class="rule" style="left:0;top:2806px;width:99px"></div>
<h2 class="sec-title" style="left:128px;top:2782px;font-size:35px">Compare</h2>
<div class="select" style="left:735px;top:2794px;width:175px;height:44px"><span style="display:flex;gap:8px;align-items:center"><svg width="16" height="16" viewBox="0 0 16 16"><circle cx="8" cy="8" r="6" fill="none" stroke="#9aa6aa"/></svg>Binova</span><svg width="12" height="8" viewBox="0 0 12 8"><path d="M1 1l5 5 5-5" stroke="#00AB8E" stroke-width="2" fill="none"/></svg></div>
<div class="select" style="left:925px;top:2794px;width:174px;height:44px"><span style="display:flex;gap:8px;align-items:center"><svg width="16" height="16" viewBox="0 0 16 16"><circle cx="8" cy="8" r="6" fill="none" stroke="#9aa6aa"/></svg>Coinvale</span><svg width="12" height="8" viewBox="0 0 12 8"><path d="M1 1l5 5 5-5" stroke="#00AB8E" stroke-width="2" fill="none"/></svg></div>

<div class="panel" style="left:121px;top:2876px;width:333px;height:682px">
  <svg class="abs" style="left:0;top:0" width="333" height="260" viewBox="0 0 333 260" font-family="Inter,sans-serif" font-size="11" fill="#00AB8E" font-weight="500">
    <g fill="none" stroke="#00AB8E" stroke-width="1.5">
      <polygon points="163,48 241,105 211,196 115,196 85,105"/>
      <polygon points="163,68 222,111 199,180 127,180 104,111" stroke="#67D7C9"/>
      <polygon points="163,89 202,117 187,163 139,163 124,117" stroke="#C6EFE9"/>
    </g>
    <g stroke="#C6EFE9"><line x1="163" y1="130" x2="163" y2="48"/><line x1="163" y1="130" x2="241" y2="105"/><line x1="163" y1="130" x2="211" y2="196"/><line x1="163" y1="130" x2="115" y2="196"/><line x1="163" y1="130" x2="85" y2="105"/></g>
    <polygon points="163,56 218,112 187,163 134,170 101,110" fill="#67D7C9" fill-opacity=".55" stroke="#00BBA5"/>
    <polygon points="163,81 233,107 199,180 139,163 116,115" fill="#00BBA5" fill-opacity=".35" stroke="#00AB8E"/>
    <g fill="#00AB8E"><circle cx="163" cy="48" r="3"/><circle cx="241" cy="105" r="3"/><circle cx="211" cy="196" r="3"/><circle cx="115" cy="196" r="3"/><circle cx="85" cy="105" r="3"/></g>
    <text x="163" y="38" text-anchor="middle">Fees</text>
    <text x="246" y="148">Features</text>
    <text x="34" y="110">Security</text>
    <text x="79" y="226">Deposits</text>
    <text x="178" y="229">Withdrawals</text>
  </svg>
  <table class="score-table">
    <thead><tr><th></th><th>Binova</th><th>Coinvale</th></tr></thead>
    <tbody>
      <tr><td>Fees</td><td style="text-align:center">9/10</td><td style="text-align:center">9/10</td></tr>
      <tr><td>Security</td><td style="text-align:center">9/10</td><td style="text-align:center">9/10</td></tr>
      <tr><td>Features</td><td style="text-align:center">9/10</td><td style="text-align:center">9/10</td></tr>
      <tr><td>Deposits</td><td style="text-align:center">9/10</td><td style="text-align:center">9/10</td></tr>
      <tr><td>Withdrawals</td><td style="text-align:center">9/10</td><td style="text-align:center">9/10</td></tr>
    </tbody>
  </table>
</div>

<div class="panel" style="left:476px;top:2876px;width:621px;height:682px">
  <div class="acc-head" style="top:38px"><svg width="22" height="18" viewBox="0 0 22 18"><rect x="1" y="10" width="5" height="7" fill="#67D7C9"/><rect x="8" y="3" width="5" height="14" fill="#00AB8E"/><rect x="15" y="7" width="5" height="10" fill="#67D7C9"/></svg>FEATURES<svg class="chev" width="16" height="10" viewBox="0 0 16 10"><path d="M1 9l7-7 7 7" stroke="#00AB8E" stroke-width="2" fill="none"/></svg></div>
  <div class="feat-row shade" style="top:73px"><span># of Coins</span><span>BAC</span><span>BAC</span></div>
  <div class="feat-row" style="top:121px"><span># of Futures</span><span>ABC</span><span>ABC</span></div>
  <div class="feat-row shade" style="top:169px"><span>Trading Bots</span><span>XYX</span><span>XYX</span></div>
  <div class="feat-row" style="top:216px"><span>Copy Trading</span><span>MIN</span><span>MIN</span></div>
  <div class="feat-row shade" style="top:264px"><span>24/7 Support</span><span>UBP</span><span>UBP</span></div>
  <div class="acc-head" style="top:358px"><svg width="18" height="20" viewBox="0 0 14 16"><path d="M7 1L1 3.5V8c0 3.5 3 6 6 7 3-1 6-3.5 6-7V3.5z" fill="#00AB8E"/></svg>SECURITY<svg class="chev" width="16" height="10" viewBox="0 0 16 10"><path d="M1 1l7 7 7-7" stroke="#00AB8E" stroke-width="2" fill="none"/></svg></div>
  <div class="acc-line" style="top:401px"></div>
  <div class="acc-head" style="top:431px"><svg width="20" height="20" viewBox="0 0 20 20"><circle cx="10" cy="10" r="9" fill="#00AB8E"/><text x="10" y="14.5" font-size="12" font-weight="700" text-anchor="middle" fill="#fff" font-family="Inter,sans-serif">$</text></svg>FEES<svg class="chev" width="16" height="10" viewBox="0 0 16 10"><path d="M1 1l7 7 7-7" stroke="#00AB8E" stroke-width="2" fill="none"/></svg></div>
  <div class="acc-line" style="top:474px"></div>
  <div class="acc-head" style="top:503px"><svg width="20" height="20" viewBox="0 0 20 20"><rect x="2" y="2" width="16" height="5" fill="#00AB8E"/><rect x="4" y="8" width="12" height="10" fill="#00AB8E"/><path d="M10 10v6M7 13l3 3 3-3" stroke="#fff" stroke-width="1.5" fill="none"/></svg>DEPOSITS<svg class="chev" width="16" height="10" viewBox="0 0 16 10"><path d="M1 1l7 7 7-7" stroke="#00AB8E" stroke-width="2" fill="none"/></svg></div>
  <div class="acc-line" style="top:546px"></div>
  <div class="acc-head" style="top:576px"><svg width="24" height="18" viewBox="0 0 24 18"><rect x="1" y="3" width="20" height="12" rx="1" fill="#00AB8E"/><circle cx="11" cy="9" r="3.5" fill="#fff"/><rect x="20" y="6" width="3" height="6" fill="#67D7C9"/></svg>WITHDRAWALS<svg class="chev" width="16" height="10" viewBox="0 0 16 10"><path d="M1 1l7 7 7-7" stroke="#00AB8E" stroke-width="2" fill="none"/></svg></div>
</div>

<!-- FAQ -->
<div class="abs" style="left:624px;top:3624px;width:2px;height:74px;background:var(--green)"></div>
<div class="abs" style="left:620px;top:3694px;width:10px;height:10px;border-radius:50%;background:var(--green)"></div>
<h2 class="faq-title">Frequently Asked <span>Questions</span></h2>
<div class="faq" style="top:3836px">What Are Crypto Exchanges?<svg width="16" height="10" viewBox="0 0 16 10"><path d="M1 1l7 7 7-7" stroke="#00AB8E" stroke-width="2" fill="none"/></svg></div>
<div class="faq" style="top:3917px">How To Choose a Crypto Exchange?<svg width="16" height="10" viewBox="0 0 16 10"><path d="M1 1l7 7 7-7" stroke="#00AB8E" stroke-width="2" fill="none"/></svg></div>
<div class="faq" style="top:3997px">How is this data tracked?<svg width="16" height="10" viewBox="0 0 16 10"><path d="M1 1l7 7 7-7" stroke="#00AB8E" stroke-width="2" fill="none"/></svg></div>
<div class="faq" style="top:4078px">How often is this page updated?<svg width="16" height="10" viewBox="0 0 16 10"><path d="M1 1l7 7 7-7" stroke="#00AB8E" stroke-width="2" fill="none"/></svg></div>
<div class="faq open" style="top:4157px">How to Crypto Exchanges?
  <p>Lorem ipsum dolor sit amet, consectetur adipiscing elit, sed do eiusmod tempor incididunt ut labore et dolore magna aliqua. Quis ipsum suspendisse ultrices gravida. Risus commodo viverra maecenas accumsan lacus vel facilisis.</p>
  <svg width="16" height="10" viewBox="0 0 16 10"><path d="M1 9l7-7 7 7" stroke="#00AB8E" stroke-width="2" fill="none"/></svg></div>

<footer class="site-footer">
  <div class="fbrand">Crypto Exchange</div>
  <p class="fabout">Lorem ipsum dolor sit amet, consectetur adipiscing elit, sed do eiusmod tempor incididunt ut labore</p>
  <div class="copy">© 2025 Crypto Exchange. All Rights Reserved</div>
  <div class="fcol" style="left:470px"><h4>Navigation</h4><a href="#">Crypto Currencies</a><a href="#">Exchanges</a><a href="#">Learn</a><a href="#">How it Works</a><a href="#">API</a><a href="#">Resources</a></div>
  <div class="fcol" style="left:684px"><h4>Resources</h4><a href="#">Terms &amp; Conditions</a><a href="#">FAQ</a><a href="#">Privacy Police</a><a href="#">Blog</a><a href="#">Sitemap</a><a href="#">Contact Us</a></div>
  <div class="fcol" style="left:907px"><h4>Follow us</h4></div>
  <div class="social" aria-label="Social channels"><i></i><i></i><i></i><i></i></div>
</footer>

</div>
</body>
</html>
```